Lead Sales Portal Needs to Generate B2B Signup's

We are looking for banner ad designs to drive new business (B2B) traffic to our insurance and mortgage industry self serve lead sites. The sites are HomeLoanProspectHub.com and CoverageProspectHub.com, and we service over 45,000 insurance agents and mortgage lenders in a self serve lead portal model. We want our banners to generate more of these clients.

Our clients come to our sites, browse our database and then pick out and purchase the consumer leads that they need to generate new business.

We advertise extensively on Zorvix and on other PPC platforms, and our existing banners are looking really tired.

Some of the ad copy that works well for us is:

Cherry Pick Your Life Leads - Why Pay More Than $3.50 For Life Insurance Leads?
Sign up today and we'll match up to $250

Agents - Here's $250 For New Clients. Cherry Pick Your Life Insurance Leads & Save! Sign up today and we'll match up to $250

One of our Landing Pages that performs well is here:
http://www.coverageprospecthub.com/lp/008/

One of our competitors ad's are here:

http://www.tralvo.com/search/results?q=PolicyBeacon&ad=427360

We're looking for a design that is eye catching, uses our "Deeply Discounted Leads" and our "$250 match bonus"

This is the second contest that we have for the same sites. The previous designs were great and really performed well, so we are looking for new designs now that 6 months have passed. I have uploaded some winning banners from the last group for your information.
Updates

Project Deadline Extended
Reason: I've been asked by some of the designers to delay a day to get their designs in. I'm happy to do it!

Target Market(s)

These are insurance agents and mortgage lenders. All of our clients are business' or individuals within the business. This is a B2B campaign, so we need something that is professional and upscale. These are NOT consumer facing ad's!

Industry/Entity Type

Insurance

Font styles to use
Sans Serif

Requirements
Must have
• We must have the logos for the sites in the banners. Also, we must have a call to action arrow and "Go" button. Some animation is necessary, (especially around the arrow and the GO button).

One or two designs.

File type

.JPEG
.JPG
.PNG
.GIF

File size

150 KB or smaller

Image sizes

Vertical rectangle: 240 x 400
Mobile leaderboard: 320 x 50
Banner: 468 x 60
Leaderboard: 728 x 90
Square: 250 x 250
Small square: 200 x 200
Large rectangle: 336 x 280
Inline rectangle: 300 x 250
Skyscraper: 120 x 600
Wide skyscraper: 160 x 600
Half-page: 300 x 600
Large leaderboard: 970 x 90

```html
<!DOCTYPE html>
<html lang="en">
<head>
<meta charset="utf-8">
<title>Coverage Prospect Hub – Cherry Pick Banners</title>
<link rel="stylesheet" href="https://fonts.googleapis.com/css2?family=Oswald:wght@400;500&family=Open+Sans:wght@400;600;700&display=swap">
<style>
  :root {
    --backdrop: #3a1c10;
    --backdrop-edge: #24100a;
    --panel: #2a2c2f;
    --panel-dark: #1f2123;
    --header: #2e3033;
    --lime: #8cc11f;
    --lime-band: #86bb1a;
    --ink: #17190f;
    --white: #ffffff;
    --go-red: #e01a12;
    --go-red-dark: #a80d08;
    --photo-light: #eef3f7;
    --photo-mid: #b9cfe0;
    --photo-dark: #6b8aa6;
  }
  * { box-sizing: border-box; margin: 0; padding: 0; }
  html, body {
    width: 1193px; height: 1200px; overflow: hidden;
    background: radial-gradient(ellipse at 50% 40%, var(--backdrop), var(--backdrop-edge));
    font-family: "Open Sans", Arial, sans-serif;
  }
  .stage {
    position: absolute; left: 0; top: 0;
    width: 660px; height: 664px;
    transform: scale(1.8076); transform-origin: 0 0;
  }
  .banner {
    position: absolute; overflow: hidden;
    background: linear-gradient(180deg, var(--panel), var(--panel-dark));
    box-shadow: 0 2px 8px rgba(0,0,0,.6);
    color: var(--white); text-align: center;
  }
  .brand {
    display: flex; align-items: center; justify-content: center; gap: 5px;
    background: var(--header); font-size: 11.5px; font-weight: 400; color: var(--white);
  }
  .brand-dot { width: 17px; height: 17px; border-radius: 50%; background: var(--white); }
  .photo {
    position: absolute;
    background: linear-gradient(160deg, var(--photo-light) 0%, var(--photo-mid) 55%, var(--photo-dark) 100%);
  }
  .headline {
    font-family: "Oswald", "Arial Narrow", sans-serif; font-weight: 400;
    color: var(--lime); line-height: 1;
  }
  .subhead { font-weight: 600; letter-spacing: .5px; line-height: 1; }
  .question { font-weight: 400; line-height: 1.02; letter-spacing: .2px; }
  .offer {
    position: absolute; background: var(--lime-band); color: var(--ink);
    font-family: "Oswald", "Arial Narrow", sans-serif; font-weight: 400;
    line-height: 1.1; display: flex; align-items: center; justify-content: center;
  }
  .go {
    position: absolute; display: flex; align-items: center; justify-content: center; gap: 6px;
    background: linear-gradient(180deg, #f0372c, var(--go-red) 60%, var(--go-red-dark));
    border: 1px solid #ffffff55; border-radius: 2px;
    font-family: "Oswald", "Arial Narrow", sans-serif; font-weight: 500; font-size: 13px; color: var(--white);
  }
  .go svg { width: 11px; height: 11px; }

  /* 160 x 600 skyscraper */
  .sky { left: 90px; top: 27px; width: 160px; height: 600px; }
  .sky .brand { height: 43px; }
  .sky .photo { left: 0; top: 43px; width: 160px; height: 225px; }
  .sky .divider { position: absolute; left: 0; top: 268px; width: 160px; height: 8px;
    background: linear-gradient(90deg, #3c3e41, #8a8c8f 50%, #3c3e41); opacity: .6; }
  .sky .headline { position: absolute; top: 300px; width: 100%; font-size: 28px; }
  .sky .subhead { position: absolute; top: 333px; width: 100%; font-size: 14.5px; }
  .sky .question { position: absolute; top: 372px; width: 100%; font-size: 16.5px; }
  .sky .offer { left: 0; top: 461px; width: 160px; height: 43px; font-size: 13px; }
  .sky .offer-notch { position: absolute; left: 73px; top: 503px; }
  .sky .contact { position: absolute; top: 529px; width: 100%; font-size: 9.5px; font-weight: 700; line-height: 1.6; }
  .sky .go { left: 52px; top: 566px; width: 57px; height: 21px; }

  /* 300 x 250 inline rectangle */
  .rect { left: 269px; top: 27px; width: 301px; height: 250px; }
  .rect .copy { position: absolute; left: 0; top: 0; width: 157px; height: 250px; }
  .rect .brand { height: 37px; }
  .rect .photo { left: 157px; top: 0; width: 144px; height: 250px; }
  .rect .headline { position: absolute; top: 55px; width: 100%; font-size: 26px; }
  .rect .subhead { position: absolute; top: 85px; width: 100%; font-size: 13px; }
  .rect .question { position: absolute; top: 124px; width: 100%; font-size: 14px; }
  .rect .offer { left: 0; top: 200px; width: 157px; height: 46px; font-size: 12.5px; }
  .rect .offer-arrow { position: absolute; left: 157px; top: 205px; }
  .rect .go { left: 174px; top: 219px; width: 58px; height: 22px; }
</style>
</head>
<body>
<main class="stage">

  <section class="banner sky" aria-label="Skyscraper banner 160 by 600">
    <div class="brand"><span class="brand-dot"></span><span>Coverage Prospect Hub</span></div>
    <div class="photo" role="img" aria-label="Photo of a smiling agent in a blue shirt talking on the phone at his desk"></div>
    <div class="divider"></div>
    <h1 class="headline">CHERRY PICK</h1>
    <p class="subhead">YOUR LIFE LEADS</p>
    <p class="question">WHY PAY MORE<br>THAN $3.50 FOR<br>LIFE INSURANCE<br>LEADS?</p>
    <p class="offer">SIGN UP TODAY AND<br>WE'LL MATCH UP TO $250</p>
    <svg class="offer-notch" width="14" height="8" viewBox="0 0 14 8"><path d="M0 0h14L7 8z" fill="#86bb1a"/></svg>
    <p class="contact">(877) 555-0142<br>www.homeloanprospecthub.com</p>
    <a class="go">GO <svg viewBox="0 0 12 12"><circle cx="6" cy="6" r="6" fill="#fff"/><path d="M5 3.2 7.8 6 5 8.8" stroke="#e01a12" stroke-width="1.8" fill="none"/></svg></a>
  </section>

  <section class="banner rect" aria-label="Inline rectangle banner 300 by 250">
    <div class="copy">
      <div class="brand"><span class="brand-dot"></span><span>Coverage Prospect Hub</span></div>
      <h1 class="headline">CHERRY PICK</h1>
      <p class="subhead">YOUR LIFE LEADS</p>
      <p class="question">WHY PAY MORE<br>THAN $3.50 FOR<br>LIFE INSURANCE<br>LEADS?</p>
      <p class="offer">SIGN UP TODAY AND<br>WE'LL MATCH UP TO $250</p>
    </div>
    <div class="photo" role="img" aria-label="Photo of a smiling agent in a blue shirt talking on the phone"></div>
    <svg class="offer-arrow" width="9" height="18" viewBox="0 0 9 18"><path d="M0 0l9 9-9 9z" fill="#86bb1a"/></svg>
    <a class="go">GO <svg viewBox="0 0 12 12"><circle cx="6" cy="6" r="6" fill="#fff"/><path d="M5 3.2 7.8 6 5 8.8" stroke="#e01a12" stroke-width="1.8" fill="none"/></svg></a>
  </section>

</main>
</body>
</html>
```